business card for LWR pty ltd

We require a business card that stands out . I have included our company flyer and would like the services listed to be put on the card so when we Give out the cards to customers they have an idea of services we provide. need the winning design to be in editable photo shop format, editable iMac pages format or editable windows publisher format, so that I can enter in names, email addresses, phone numbers etc myself. I have included a pdf documents of info / items needed on the card to use as reference please.
Updates

need more submissions

Need extra days to review

Sick

Target Market(s)

new customers

Contact Information for Business Card

details are on attached business card requirements file

Requirements
Must have
• I have attached a list of must haves

```html
<!DOCTYPE html>
<html lang="en">
<head>
<meta charset="utf-8">
<title>LWR pty ltd – Business Card</title>
<link href="https://fonts.googleapis.com/css2?family=Arimo:wght@400;700&display=swap" rel="stylesheet">
<style>
  :root{
    --bg:#2a2a2c;
    --card:#070707;
    --mesh-1:#1d1d20;
    --mesh-2:#050505;
    --gold:#d9b57e;
    --white:#f4f4f4;
    --soft:#cfcfcf;
    --earth-1:#8a5d36;
    --earth-2:#5a3a1f;
    --sky:#0c0c0c;
  }
  *{box-sizing:border-box;margin:0;padding:0}
  html,body{width:1200px;height:1015px;overflow:hidden;background:var(--bg)}
  body{font-family:"Arimo",Arial,sans-serif;position:relative}
  .card{
    position:absolute;left:220px;width:760px;height:464px;
    background:var(--card);overflow:hidden;
    box-shadow:0 10px 30px rgba(0,0,0,.45);
  }
  .card--back{top:26px}
  .card--front{top:525px}

  /* back side */
  .card--back .texture{
    position:absolute;inset:0;
    background:radial-gradient(ellipse at 75% 15%,var(--mesh-1) 0%,var(--mesh-2) 70%);
  }
  .services{
    position:absolute;left:62px;top:78px;list-style:none;
  }
  .services li{
    color:var(--white);font-size:22px;line-height:30.5px;
    text-transform:uppercase;letter-spacing:.3px;
    display:flex;align-items:center;
  }
  .services li::before{
    content:"";width:11px;height:11px;border-radius:50%;
    background:var(--gold);margin-right:16px;flex:none;
  }

  /* front side */
  .card--front .texture{
    position:absolute;left:260px;top:60px;width:420px;height:260px;
    background:radial-gradient(ellipse at center,var(--mesh-1) 0%,transparent 70%);
  }
  .photo{
    position:absolute;left:170px;right:0;top:215px;bottom:0;
    background:
      linear-gradient(180deg,var(--card) 0%,rgba(7,7,7,.2) 35%,transparent 55%),
      linear-gradient(180deg,#2b2620 40%,var(--earth-1) 72%,var(--earth-2) 100%);
  }
  .person{position:absolute;left:48px;top:150px}
  .person__name{
    color:var(--gold);font-weight:700;font-size:36px;letter-spacing:.5px;
    text-transform:uppercase;
  }
  .person__role{color:var(--white);font-size:21px;margin-top:6px}
  .contact{position:absolute;left:360px;top:34px;list-style:none}
  .contact li{
    display:flex;align-items:center;color:var(--white);
    font-size:21px;line-height:30px;
  }
  .contact svg{width:20px;height:20px;margin-right:10px;flex:none}
  .brand{
    position:absolute;left:380px;top:168px;
    display:flex;align-items:center;gap:12px;
    color:var(--soft);font-weight:700;font-size:40px;
  }
  .brand__mark{width:22px;height:22px;border-radius:50%;background:var(--soft)}
  .address{
    position:absolute;right:40px;bottom:46px;
    color:var(--white);font-size:21px;
  }
</style>
</head>
<body>

<section class="card card--back" aria-label="Business card back – services">
  <div class="texture"></div>
  <ul class="services">
    <li>Over size loads/hot shot loads</li>
    <li>Heavy vehicle recovery services</li>
    <li>Potable water deliveries</li>
    <li>Road building/maintenance</li>
    <li>Earthworks</li>
    <li>Sand &amp; metal supply &amp; cartage</li>
    <li>Road train tippers</li>
    <li>Road train tankers</li>
    <li>Road train flat tops</li>
    <li>Drop deck trailers</li>
    <li>Mine site accredited equipment &amp; operators</li>
  </ul>
</section>

<section class="card card--front" aria-label="Business card front – contact details">
  <div class="texture"></div>
  <div class="photo" role="img" aria-label="Photograph of a road train truck with tipper trailers on red outback dirt"></div>

  <div class="person">
    <p class="person__name">Daniel Harker</p>
    <p class="person__role">Director</p>
  </div>

  <ul class="contact">
    <li>
      <svg viewBox="0 0 24 24" aria-hidden="true"><path fill="var(--gold)" d="M6.6 10.8a15 15 0 0 0 6.6 6.6l2.2-2.2c.3-.3.7-.4 1-.2 1.1.4 2.3.6 3.6.6.6 0 1 .4 1 1V20c0 .6-.4 1-1 1A17 17 0 0 1 3 4c0-.6.4-1 1-1h3.5c.6 0 1 .4 1 1 0 1.3.2 2.5.6 3.6.1.3 0 .7-.2 1z"/></svg>
      000 444 000
    </li>
    <li>
      <svg viewBox="0 0 24 24" aria-hidden="true"><rect x="2" y="5" width="20" height="14" rx="1" fill="var(--gold)"/><path d="M2 6l10 7 10-7" fill="none" stroke="var(--card)" stroke-width="1.6"/></svg>
      email@lwrhaulage.com.au
    </li>
    <li>
      <svg viewBox="0 0 24 24" aria-hidden="true"><circle cx="12" cy="12" r="9.5" fill="none" stroke="var(--gold)" stroke-width="2"/><ellipse cx="12" cy="12" rx="4" ry="9.5" fill="none" stroke="var(--gold)" stroke-width="1.6"/><path d="M2.5 12h19M4 7.5h16M4 16.5h16" stroke="var(--gold)" stroke-width="1.4"/></svg>
      www.lwrhaulage.com.au
    </li>
  </ul>

  <div class="brand">
    <span class="brand__mark" aria-hidden="true"></span>
    <span class="brand__name">LWR pty ltd</span>
  </div>

  <p class="address">Lot 444 example address Australia</p>
</section>

</body>
</html>
```